Pest Control Company needs business card!

Hi there, we need a business card designed for our new Pest Control Company. Ideally this card will be simple, yet feel elegant and high end. We want to use the colours Orange, Black and White. Please see our attached logo for the exact colours.

Business card details:

Phone - 0461 275 804
Name - Gavin Holloway
Email - Info@steadfastverminguard.com.au

We would also like to include the following list with dot points:

SERVICES / INSPECTIONS

Termites, Wood Borers, Ants, Cockroaches, Spiders, Fleas, Mice, Rats, Bed Bugs, & More!

```html
<!DOCTYPE html>
<html lang="en">
<head>
<meta charset="utf-8">
<title>Steadfast Vermin Guard – Business Card</title>
<link href="https://fonts.googleapis.com/css2?family=Montserrat:wght@400;500;600;700;800&display=swap" rel="stylesheet">
<style>
  :root{
    --brand-orange:#ee4a1c;
    --brand-orange-light:#f6682f;
    --ink:#1c1c1c;
    --paper:#ffffff;
    --muted:#3a3a3a;
    --backdrop:#e9e9eb;
  }
  *{box-sizing:border-box;margin:0;padding:0}
  html,body{width:1200px;height:912px;overflow:hidden}
  body{
    background:var(--backdrop);
    font-family:'Montserrat',sans-serif;
    display:flex;flex-direction:column;align-items:center;justify-content:center;gap:40px;
  }
  .card{
    position:relative;width:660px;height:402px;border-radius:22px;overflow:hidden;
    box-shadow:0 10px 26px rgba(0,0,0,.18);
  }
  .brand-name{
    display:flex;align-items:center;gap:14px;
    font-weight:800;text-transform:uppercase;line-height:1.02;
  }
  .brand-name__dot{width:22px;height:22px;border-radius:50%;background:currentColor;flex:none}

  /* Front */
  .card--front{
    background:linear-gradient(120deg,var(--brand-orange-light) 0%,var(--brand-orange) 45%,var(--brand-orange) 100%);
    color:var(--paper);
    display:flex;flex-direction:column;align-items:center;justify-content:center;text-align:center;
  }
  .card--front .brand-name{font-size:34px;letter-spacing:.5px}
  .services__title{margin-top:34px;font-size:19px;font-weight:500;letter-spacing:1px}
  .services__list{margin-top:12px;font-size:14.5px;font-weight:400;letter-spacing:.8px;line-height:1.55;text-transform:uppercase}

  /* Back */
  .card--back{background:var(--paper);color:var(--ink)}
  .card--back .brand-name{
    position:absolute;left:44px;top:96px;width:250px;
    font-size:28px;color:var(--ink);align-items:flex-start;
  }
  .card--back .brand-name__dot{margin-top:4px}
  .contact-person{position:absolute;right:44px;top:58px;text-align:right}
  .contact-person__name{font-size:24px;font-weight:500;color:var(--brand-orange);text-transform:uppercase;letter-spacing:.5px;line-height:1.1}
  .contact-person__role{margin-top:6px;font-size:15px;color:var(--muted)}
  .edge-mark{position:absolute;right:0;top:58px;width:10px;height:32px;background:var(--brand-orange)}
  .divider{position:absolute;left:230px;right:40px;top:250px;height:2px;background:var(--brand-orange)}
  .contact{position:absolute;left:230px;top:276px;list-style:none;font-size:18px;color:var(--muted)}
  .contact__item{display:flex;align-items:center;gap:10px;margin-bottom:8px}
  .contact__icon{width:16px;height:16px;flex:none}
</style>
</head>
<body>

<section class="card card--front">
  <div class="brand-name"><span class="brand-name__dot"></span>Steadfast Vermin Guard</div>
  <p class="services__title">SERVICES / INSPECTIONS</p>
  <p class="services__list">Termites | Wood Borers | Ants | Cockroaches<br>Spiders | Fleas | Mice | Rats | Bed Bugs | &amp; More!</p>
</section>

<section class="card card--back">
  <div class="brand-name"><span class="brand-name__dot"></span><span>Steadfast Vermin Guard</span></div>
  <span class="edge-mark"></span>
  <div class="contact-person">
    <p class="contact-person__name">Gavin Holloway</p>
    <p class="contact-person__role">Director</p>
  </div>
  <span class="divider"></span>
  <ul class="contact">
    <li class="contact__item">
      <svg class="contact__icon" viewBox="0 0 24 24"><path fill="#ee4a1c" d="M6.6 10.8a15 15 0 0 0 6.6 6.6l2.2-2.2a1 1 0 0 1 1-.25 11.4 11.4 0 0 0 3.6.57 1 1 0 0 1 1 1V20a1 1 0 0 1-1 1A17 17 0 0 1 3 4a1 1 0 0 1 1-1h3.5a1 1 0 0 1 1 1c0 1.25.2 2.45.57 3.57a1 1 0 0 1-.25 1z"/></svg>
      0461 275 804
    </li>
    <li class="contact__item">
      <svg class="contact__icon" viewBox="0 0 24 24"><rect x="3" y="5" width="18" height="14" rx="1.5" fill="none" stroke="#ee4a1c" stroke-width="2"/><path d="M3.5 6l8.5 7 8.5-7" fill="none" stroke="#ee4a1c" stroke-width="2"/></svg>
      Info@steadfastverminguard.com.au
    </li>
  </ul>
</section>

</body>
</html>
```